Software as a Service to manage Home Care Management

We need a web site designed for Home Care Management Software as a Service product, that facilitates Home Care organizations to manage and schedule carers to visit client homes. We want a modern look and feel using our existing logo.

Target Market(s)

Home Care Management organizations. Product is similar to: https://wovenpath.co/

Coding

Coded - Design and coding required

Number of Pages Required

3 page

```html
<!DOCTYPE html>
<html lang="en">
<head>
<meta charset="utf-8">
<title>Hearthline – Home Care Scheduling</title>
<link href="https://fonts.googleapis.com/css2?family=Lato:wght@400;700&family=Open+Sans:wght@400;600&display=swap" rel="stylesheet">
<style>
:root{
  --magenta:#b01f52;
  --magenta-deep:#9c1444;
  --pink:#ef6593;
  --pink-soft:#f6a9c4;
  --pink-pale:#fde6ee;
  --ink:#1d1d1f;
  --text:#444;
  --muted:#9a9a9a;
  --white:#fff;
  --btn:linear-gradient(90deg,#f2709b,#e24b7e);
}
*{box-sizing:border-box;margin:0;padding:0}
html,body{width:1200px;height:2597px;overflow:hidden}
body{position:relative;background:var(--white);font-family:'Lato',sans-serif;color:var(--ink)}
.abs{position:absolute}
.btn{position:absolute;display:flex;align-items:center;justify-content:center;background:var(--btn);color:var(--white);border-radius:17px;font-size:11px;font-weight:700;box-shadow:0 6px 14px rgba(226,75,126,.35)}

/* hero */
.hero{position:absolute;left:0;top:0;width:1200px;height:563px;overflow:hidden;box-shadow:0 18px 30px -18px rgba(0,0,0,.25)}
.hero svg{position:absolute;left:0;top:0}
.brand{position:absolute;left:118px;top:50px;display:flex;align-items:center;gap:8px;font-family:'Lato',serif;font-size:15px;font-weight:700;color:var(--magenta)}
.brand i{width:12px;height:12px;background:var(--magenta);border-radius:50%}
.nav{position:absolute;top:56px;display:flex;gap:26px;left:766px;font-size:11px;color:var(--white);font-family:'Open Sans',sans-serif;font-weight:600}
.nav-contact{position:absolute;left:963px;top:52px;width:95px;height:28px;background:var(--white);color:var(--pink);border-radius:14px;font-size:11px;font-family:'Open Sans',sans-serif;display:flex;align-items:center;justify-content:center}
.hero-title{position:absolute;left:218px;top:232px;font-size:31px;font-weight:400;line-height:33px;color:var(--ink)}
.hero-text{position:absolute;left:218px;top:314px;width:320px;font-size:12.5px;line-height:22px;color:#333;font-family:'Open Sans',sans-serif}
.hero-photo{position:absolute;left:663px;top:165px;width:437px;height:398px;border-radius:200px 200px 0 0;background:linear-gradient(180deg,#d9a99a,#4f5b6a 70%,#3b4452)}

/* audience cards */
.card{position:absolute;top:680px;width:221px;height:258px;background:var(--white);border-radius:0 0 28px 0;box-shadow:0 10px 30px rgba(0,0,0,.08);text-align:center}
.card svg{margin-top:28px}
.card h3{font-size:14px;font-weight:400;margin-top:12px}
.card p{font-size:10.5px;line-height:18px;color:#333;margin-top:6px;padding:0 20px;font-family:'Open Sans',sans-serif}
.card .btn{left:52px;top:193px;width:116px;height:34px;font-size:10px}

/* work */
.heart{position:absolute;left:944px;top:1025px}
.video-frame{position:absolute;left:240px;top:1118px;width:315px;height:316px;background:var(--pink-soft);border-radius:0 0 0 26px}
.video{position:absolute;left:229px;top:1107px;width:315px;height:314px;border-radius:0 0 0 26px;background:linear-gradient(135deg,#6e6e70,#b9a9a0 50%,#8a7a80)}
.play{position:absolute;left:358px;top:1237px;width:52px;height:52px;border-radius:50%;background:rgba(255,255,255,.85)}
.work-title{position:absolute;left:601px;top:1148px;font-size:30px;font-weight:400}
.work-text{position:absolute;left:601px;top:1206px;width:365px;font-size:11px;line-height:22px;color:#333;font-family:'Open Sans',sans-serif}
.work-text p+p{margin-top:12px}

.tablet{position:absolute;left:251px;top:1524px;width:739px;height:511px;border-radius:40px;background:linear-gradient(135deg,#d92a4a,#a8184e);transform:skewY(-4deg) rotate(4deg);box-shadow:0 30px 40px rgba(0,0,0,.2)}

/* features */
.feature{position:absolute;top:2088px;width:230px;text-align:center}
.feature h4{font-size:12px;font-weight:400;color:#555;margin-top:24px}
.feature p{font-size:8.5px;line-height:17px;color:var(--muted);margin-top:6px;font-family:'Open Sans',sans-serif}

/* footer */
.footer-bg{position:absolute;left:0;top:2300px}
.stats{position:absolute;left:249px;top:2294px;width:702px;height:89px;background:linear-gradient(90deg,var(--magenta),#d84375);display:flex;justify-content:space-around;padding:0 40px;color:var(--white);box-shadow:0 12px 22px rgba(0,0,0,.15)}
.stat{text-align:center;padding-top:22px}
.stat b{display:block;font-size:26px;font-weight:400;line-height:28px}
.stat span{font-size:10px}
.footer-brand{position:absolute;left:322px;top:2421px;display:flex;align-items:center;gap:7px;font-size:13px;font-weight:700;color:var(--magenta)}
.footer-brand i{width:10px;height:10px;border-radius:50%;background:var(--magenta)}
.footer-text{position:absolute;left:320px;top:2466px;width:200px;font-size:8.5px;line-height:17px;color:var(--white);font-family:'Open Sans',sans-serif}
.social{position:absolute;left:320px;top:2549px;display:flex;gap:14px}
.social i{width:12px;height:12px;border-radius:50%;background:var(--white)}
.subscribe{position:absolute;left:667px;top:2432px;width:211px;height:28px;border-radius:14px;background:rgba(255,255,255,.3);display:flex;align-items:center;font-size:9px;color:var(--white);font-family:'Open Sans',sans-serif}
.subscribe span{padding-left:28px;flex:1}
.subscribe b{width:96px;height:28px;border-radius:14px;background:var(--white);color:var(--pink);font-weight:400;display:flex;align-items:center;justify-content:center}
.contact{position:absolute;left:770px;top:2468px;font-size:8.5px;color:var(--white);font-family:'Open Sans',sans-serif}
.contact li{list-style:none;display:flex;align-items:center;gap:10px;height:21px}
.copy{position:absolute;left:0;width:1188px;top:2563px;text-align:center;font-size:10px;color:var(--white);font-family:'Open Sans',sans-serif}
</style>
</head>
<body>

<header class="hero">
  <svg width="1200" height="563" viewBox="0 0 1200 563">
    <defs>
      <linearGradient id="soft" x1="0" y1="0" x2="0" y2="1"><stop offset="0" stop-color="#fde9f1"/><stop offset="1" stop-color="#f27ca4"/></linearGradient>
      <linearGradient id="deep" x1="0" y1="0" x2="1" y2="1"><stop offset="0" stop-color="#b8255a"/><stop offset="1" stop-color="#a51b4c"/></linearGradient>
    </defs>
    <path d="M0 105 C260 92 520 150 630 300 L660 563 H0Z" fill="url(#soft)"/>
    <path d="M440 0 H1200 V563 H640 C670 380 620 230 440 0Z" fill="url(#deep)"/>
  </svg>
  <div class="brand"><i></i>Hearthline</div>
  <nav class="nav"><span>Home</span><span>About Us</span><span>Services</span></nav>
  <div class="nav-contact">Contact Us</div>
  <h1 class="hero-title">Schedule carers visits<br>to your loved ones</h1>
  <p class="hero-text">the best possible ways of supporting care staff and people at home.  We work closely with care companies to have a system that is fit for the purpose of planning, delivering and reporting homecare.</p>
  <div class="btn" style="left:218px;top:426px;width:95px;height:28px;font-weight:400;font-size:10px">Services</div>
  <div class="hero-photo" role="img" aria-label="Photo of a smiling carer walking arm in arm with an elderly man"></div>
</header>

<section class="audiences">
  <article class="card" style="left:222px">
    <svg width="48" height="48" viewBox="0 0 48 48"><circle cx="24" cy="14" r="10" fill="#e5456f"/><path d="M4 46 C4 30 44 30 44 46Z" fill="#e5456f"/><path d="M22 28 h4 l2 14 -4 4 -4 -4Z" fill="#fff"/></svg>
    <h3>For Managers</h3>
    <p>Care management tools that save your time and money. Enables you to grow your business.</p>
    <div class="btn">LEARN MORE</div>
  </article>
  <article class="card" style="left:483px">
    <svg width="54" height="48" viewBox="0 0 54 48"><path d="M27 24 C14 14 18 4 27 10 C36 4 40 14 27 24Z" fill="#e5456f"/><path d="M2 34 C10 28 18 30 26 34 H38 C42 34 42 39 38 39 H26 M34 38 L48 30 C52 28 54 32 51 35 L36 46 H2Z" fill="#e5456f"/></svg>
    <h3>For Carers</h3>
    <p>Simple and easy to use App. Rosters and care plans on the go. More time for care.</p>
    <div class="btn">LEARN MORE</div>
  </article>
  <article class="card" style="left:745px">
    <svg width="52" height="48" viewBox="0 0 52 48"><circle cx="14" cy="12" r="6" fill="#e5456f"/><circle cx="38" cy="12" r="6" fill="#e5456f"/><circle cx="26" cy="24" r="5" fill="#e5456f"/><path d="M4 46 V26 C4 18 24 18 24 26 V46Z M28 46 V26 C28 18 48 18 48 26 V46Z" fill="#e5456f"/><path d="M18 46 V36 C18 30 34 30 34 36 V46Z" fill="#c72c5b"/></svg>
    <h3>For Loved Ones</h3>
    <p>Latest information in real time, all documents in one place. Transparency for all.</p>
    <div class="btn">LEARN MORE</div>
  </article>
</section>

<section class="work">
  <svg class="heart" width="256" height="450" viewBox="0 0 256 450">
    <path d="M256 440 C150 330 30 200 30 110 C30 40 100 0 170 20 C210 30 240 50 256 70Z" fill="#e57f9f" opacity=".8"/>
    <path d="M256 420 C170 320 60 200 60 120 C60 55 120 15 185 30 C220 40 245 60 256 80Z" fill="var(--magenta-deep)"/>
  </svg>
  <div class="video-frame"></div>
  <div class="video" role="img" aria-label="Photo of a carer's hands resting on an elderly person's hand on a walking cane"></div>
  <div class="play"></div>
  <h2 class="work-title">Watch How We Work</h2>
  <div class="work-text">
    <p>Lorem ipsum dolor sit amet, consectetur adipiscing elit, sed do eiusmod tempor incididunt ut labore et dolore magna aliqua. Quis ipsum suspendisse ultrices gravida.</p>
    <p>Quis autem vel eum iure reprehenderit qui in ea voluptate velit esse quam nihil molestiae consequatur.</p>
  </div>
  <div class="btn" style="left:601px;top:1362px;width:118px;height:34px;font-weight:400;font-size:10px">Learn more</div>
</section>

<div class="tablet" role="img" aria-label="Tablet showing the app start screen on a red gradient"></div>

<section class="features">
  <div class="feature" style="left:216px">
    <svg width="44" height="40" viewBox="0 0 44 40" fill="none" stroke="#c0264f" stroke-width="2"><path d="M4 20 L20 6 L36 20 M8 17 V36 H32 V17"/><path d="M28 4 L38 8 V16 C38 22 34 25 28 27 C22 25 18 22 18 16 V8Z" fill="#fff"/><path d="M24 15 l3 3 6-6"/></svg>
    <h4>Insurance Included</h4>
    <p>Every visit is covered by our policy, so carers and families can rest easy each day.</p>
  </div>
  <div class="feature" style="left:484px">
    <svg width="40" height="40" viewBox="0 0 40 40" fill="none" stroke="#c0264f" stroke-width="2"><rect x="12" y="6" width="16" height="28" rx="2"/><path d="M18 30 h4 M4 4 h6 M30 4 h6 M4 36 h6 M30 36 h6"/><circle cx="20" cy="18" r="4"/></svg>
    <h4>Easy To Use</h4>
    <p>Clear screens and simple steps let any carer plan, log and share visits in minutes.</p>
  </div>
  <div class="feature" style="left:753px">
    <svg width="40" height="40" viewBox="0 0 40 40" fill="none" stroke="#c0264f" stroke-width="2"><path d="M6 6 H34 M10 6 V14 C10 26 30 26 30 14 V6"/><path d="M20 26 V34 M14 36 H26"/><path d="M20 11 V18 M20 21 v1"/></svg>
    <h4>Quick Respons</h4>
    <p>Alerts reach the right people fast, so urgent changes to a visit never go unseen.</p>
  </div>
</section>

<footer>
  <svg class="footer-bg" width="1200" height="297" viewBox="0 0 1200 297">
    <defs><linearGradient id="foot" x1="0" y1="0" x2="0" y2="1"><stop offset="0" stop-color="#f06a98"/><stop offset="1" stop-color="#f488ab"/></linearGradient></defs>
    <path d="M0 40 L1200 0 V297 H0Z" fill="url(#foot)"/>
  </svg>
  <div class="stats">
    <div class="stat"><b>1000+</b><span>Happy clients</span></div>
    <div class="stat"><b>156</b><span>Active services</span></div>
    <div class="stat"><b>80+</b><span>Satisfied Families</span></div>
    <div class="stat"><b>1482</b><span>Finished services</span></div>
  </div>
  <div class="footer-brand"><i></i>Hearthline</div>
  <p class="footer-text">Simple rostering for home care teams, built to keep carers, managers and families in step.</p>
  <div class="social"><i></i><i></i><i></i><i></i></div>
  <div class="subscribe"><span>Your email</span><b>Subscribe</b></div>
  <ul class="contact">
    <li><svg width="10" height="10" viewBox="0 0 10 10"><path d="M2 1 L4 3 3 4 C4 6 5 7 6 7 L7 6 9 8 8 9 C4 9 1 6 1 2Z" fill="#fff"/></svg>+ (555) 014-2290</li>
    <li><svg width="10" height="10" viewBox="0 0 10 10"><path d="M5 10 C2 6 1 5 1 4 A4 4 0 0 1 9 4 C9 5 8 6 5 10Z" fill="#fff"/><circle cx="5" cy="4" r="1.5" fill="#f06a98"/></svg>Maple Row 12, Easton</li>
    <li><svg width="10" height="10" viewBox="0 0 10 10" fill="none" stroke="#fff" stroke-width="1.2"><circle cx="5" cy="5" r="4"/><path d="M5 2.5 V5 H7"/></svg>09:00 AM – 19:00 PM</li>
    <li><svg width="10" height="10" viewBox="0 0 10 10" fill="none" stroke="#fff" stroke-width="1.2"><rect x="1" y="2" width="8" height="6"/><path d="M1 2 L5 5 9 2"/></svg>hello@hearthline.co</li>
  </ul>
  <div class="copy">2020 @ Hearthline</div>
</footer>

</body>
</html>
```